Bluestone Freight

We are a 3PL freight brokerage company looking to create a website to attract new customers. Some ideas on how other freight websites look is located at these links, https://www.marigoldhaulerline.com/services, https://quillmarkcargo.com/freight-brokerage/.
We would like to have a quote feature implemented into this website.

We specialize in heavy-haul, specialized loads, flatbed, and dry vans.

```html
<!DOCTYPE html>
<html lang="en">
<head>
<meta charset="utf-8">
<title>Bluestone Freight – Website Design</title>
<link href="https://fonts.googleapis.com/css2?family=Roboto:wght@300;400;500;700;900&display=swap" rel="stylesheet">
<style>
:root{
  --navy:#14375d;
  --gold:#b7912e;
  --light:#f4f5f7;
  --cream:#f9f6ef;
  --stage:#dfe3ea;
  --ink:#4a5566;
  --muted:#8a93a0;
  --white:#ffffff;
}
*{margin:0;padding:0;box-sizing:border-box}
html,body{width:1200px;height:3748px;overflow:hidden}
body{background:var(--stage);font-family:"Roboto",sans-serif;color:var(--ink);position:relative}
.abs{position:absolute}

/* brand board */
.brand-board{position:absolute;left:0;top:0;width:1200px;height:270px}
.brand-name{position:absolute;left:262px;top:118px;font-size:24px;font-weight:700;color:var(--navy);letter-spacing:1px;text-transform:uppercase;display:flex;align-items:center;gap:10px}
.brand-name .mark{width:16px;height:16px;background:var(--gold)}
.board-divider{position:absolute;top:92px;width:1px;height:86px;background:#c4cad4}
.board-label{position:absolute;font-size:21px;color:var(--navy);font-weight:400}
.font-names{position:absolute;left:550px;top:133px;font-size:17px;color:var(--muted);line-height:23px;font-weight:300}
.swatch{position:absolute;top:122px;width:38px;height:38px;border-radius:50%;border:1px solid #d0d5dd}
.swatch-code{position:absolute;top:166px;font-size:8px;color:var(--muted);width:50px;text-align:center}

/* flat screen preview */
.screen-preview{position:absolute;left:477px;top:276px;width:585px;height:357px;overflow:hidden;background:linear-gradient(120deg,#1c3d63 0%,#3d5a7a 55%,#6b7f96 100%)}
.screen-preview .sp-top{position:absolute;left:0;top:0;width:100%;height:24px;background:var(--navy)}
.screen-preview .sp-nav{position:absolute;left:70px;top:24px;width:445px;height:44px;background:var(--gold);display:flex;align-items:center;justify-content:space-between;padding:0 14px}
.screen-preview .sp-nav b{color:#fff;font-size:9px;font-weight:700;text-transform:uppercase}
.screen-preview .sp-links{display:flex;gap:14px;font-size:5px;color:#fff;align-items:center}
.screen-preview .sp-cta{background:var(--navy);padding:5px 9px;border-radius:10px}
.screen-preview .sp-eyebrow{position:absolute;left:80px;top:131px;font-size:5px;color:var(--gold);letter-spacing:2px}
.screen-preview .sp-h1{position:absolute;left:79px;top:140px;font-size:28px;line-height:30px;color:#fff;font-weight:700}
.screen-preview .sp-h1 .outline{color:transparent;-webkit-text-stroke:1px #fff;font-weight:300}
.screen-preview .sp-p{position:absolute;left:80px;top:214px;font-size:6px;color:#dfe5ee;line-height:10px;width:160px}
.screen-preview .sp-btn{position:absolute;left:80px;top:254px;width:22px;height:22px;border-radius:50%;background:var(--gold)}

/* page */
.page{position:absolute;left:273px;top:826px;width:654px;height:2833px;background:var(--white);overflow:hidden}
.eyebrow{font-size:4.5px;letter-spacing:1.6px;color:var(--gold);text-transform:uppercase}
.heading{font-size:20px;line-height:23px;color:var(--navy);font-weight:300}
.heading strong{font-weight:700;display:block}
.body-text{font-size:5.2px;line-height:9.5px;color:var(--ink)}
.btn{display:inline-flex;align-items:center;justify-content:center;border-radius:12px;font-size:4.5px;font-weight:700;color:#fff;text-transform:uppercase;letter-spacing:.4px}
.btn-navy{background:var(--navy)}
.btn-gold{background:var(--gold)}

.top-bar{position:absolute;left:0;top:0;width:654px;height:29px;background:var(--navy);display:flex;align-items:center;padding:0 87px;font-size:4.6px;color:#fff}
.social{display:flex;gap:5px}
.social span{width:5px;height:5px;border-radius:50%;background:#fff;opacity:.85}
.contact-items{margin-left:auto;display:flex;gap:26px}
.contact-item{display:flex;align-items:center;gap:5px}
.icon-dot{width:10px;height:10px;border-radius:50%;background:var(--gold);display:flex;align-items:center;justify-content:center}

.hero{position:absolute;left:0;top:29px;width:654px;height:390px;background:linear-gradient(110deg,#1f3c5f 0%,#365473 45%,#4f6681 70%,#6e7f93 100%)}
.main-nav{position:absolute;left:87px;top:29px;width:479px;height:48px;background:var(--gold);display:flex;align-items:center;padding:0 12px}
.nav-brand{font-size:8px;font-weight:700;color:#fff;text-transform:uppercase;letter-spacing:.5px}
.nav-links{margin-left:auto;display:flex;align-items:center;gap:22px;font-size:4.6px;color:#fff;font-weight:500;text-transform:uppercase}
.nav-cta{background:var(--navy);padding:7px 12px;border-radius:12px;font-weight:700}
.hero-eyebrow{position:absolute;left:87px;top:151px}
.hero-title{position:absolute;left:86px;top:160px;font-size:30px;line-height:34px;color:#fff;font-weight:700}
.hero-title .outline{display:block;color:transparent;-webkit-text-stroke:1px #fff;font-weight:300}
.hero-text{position:absolute;left:87px;top:235px;width:180px;font-size:6px;line-height:10px;color:#e4e9f0}
.scroll-btn{position:absolute;left:87px;top:266px;width:32px;height:32px;border-radius:50%;background:var(--gold);display:flex;align-items:center;justify-content:center}

/* about */
.about-eyebrow{position:absolute;left:87px;top:467px}
.about-heading{position:absolute;left:87px;top:478px}
.about-intro{position:absolute;left:372px;top:464px;width:196px}
.features{position:absolute;left:87px;top:574px;width:480px;height:50px}
.feature{position:absolute;top:0;display:flex;align-items:center}
.feature-num{font-size:52px;font-weight:300;color:transparent;-webkit-text-stroke:.6px #cfd5de;line-height:50px}
.feature-label{font-size:6px;color:var(--gold);margin-left:-14px}
.about-col{position:absolute;top:640px;width:190px}

/* services */
.service-tile{position:absolute;width:163px;height:163px;display:flex;flex-direction:column;align-items:center;justify-content:center;gap:12px;color:#fff;font-size:5.2px;font-weight:700;text-transform:uppercase;letter-spacing:.3px}
.tile-navy{background:var(--navy)}
.tile-gold{background:var(--gold)}
.services-panel{position:absolute;left:326px;top:760px;width:328px;height:327px;background:var(--light)}
.services-panel .eyebrow{position:absolute;left:70px;top:52px}
.services-panel .heading{position:absolute;left:70px;top:66px}
.services-panel .p1{position:absolute;left:70px;top:136px;width:190px}
.services-panel .p2{position:absolute;left:70px;top:200px;width:190px}
.services-panel .btn{position:absolute;left:70px;top:255px;width:58px;height:23px}

/* clients */
.clients-eyebrow{position:absolute;left:87px;top:1136px}
.clients-heading{position:absolute;left:87px;top:1148px}
.partner{position:absolute;display:flex;align-items:center;gap:4px}
.partner .p-circle{width:14px;height:14px;border-radius:50%;background:#c9ced6}
.partner .p-bar{width:48px;height:7px;border-radius:2px;background:#c9ced6}

.video-banner{position:absolute;left:87px;top:1239px;width:480px;height:163px;overflow:hidden;background:linear-gradient(100deg,#6c7b88 0%,#8f9aa3 50%,#a89677 100%)}
.video-banner svg.shape{position:absolute;left:0;top:0}
.play-btn{position:absolute;left:20px;top:112px;width:34px;height:34px;border-radius:50%;background:var(--gold);display:flex;align-items:center;justify-content:center}
.play-label{position:absolute;left:62px;top:126px;font-size:4.6px;color:#fff;font-weight:500;text-transform:uppercase}

/* testimonial */
.quote-text{position:absolute;left:87px;top:1463px;width:200px}
.quote-name{position:absolute;left:87px;top:1525px;font-size:5.4px;color:var(--navy);font-weight:700}
.quote-role{position:absolute;left:87px;top:1534px;font-size:4.4px;color:var(--gold)}
.testi-eyebrow{position:absolute;left:445px;top:1449px}
.testi-heading{position:absolute;left:445px;top:1459px}
.quote-mark{position:absolute;left:443px;top:1515px;font-size:60px;line-height:60px;color:var(--gold);font-weight:900;font-family:"Roboto",serif}

/* why */
.why-panel{position:absolute;left:0;top:1632px;width:326px;height:325px;background:var(--cream)}
.why-panel .eyebrow{position:absolute;left:70px;top:50px}
.why-panel .heading{position:absolute;left:70px;top:60px}
.why-item{position:absolute;left:70px;display:flex;align-items:center;gap:8px;font-size:4.4px;color:var(--gold);text-transform:uppercase;line-height:7px}
.why-icon{width:22px;height:22px;border-radius:50%;background:#ece5d3;display:flex;align-items:center;justify-content:center}
.why-panel .btn{position:absolute;left:70px;top:263px;width:58px;height:23px}
.why-photo{position:absolute;left:326px;top:1606px;width:328px;height:326px;background:linear-gradient(180deg,#6d6a5a 0%,#a3a39c 35%,#8c8f94 60%,#c4c6c8 100%)}
.years-badge{position:absolute;left:329px;top:1853px;width:77px;height:79px;background:var(--gold);color:#fff;text-align:center;padding-top:12px}
.years-badge b{display:block;font-size:28px;line-height:30px;font-weight:500}
.years-badge span{display:block;font-size:4.4px;line-height:7px;text-transform:uppercase}

/* news */
.news-eyebrow{position:absolute;left:0;top:2006px;width:654px;text-align:center}
.news-heading{position:absolute;left:0;top:2018px;width:654px;text-align:center}
.news-heading strong{display:inline}
.news-intro{position:absolute;left:0;top:2055px;width:654px;text-align:center}
.news-card{position:absolute;top:2092px;width:146px}
.news-img{width:146px;height:96px;border:3px solid #e8eaee}
.news-title{margin-top:14px;font-size:6px;color:var(--navy);font-weight:500}
.news-meta{margin-top:4px;font-size:4px;color:var(--muted);text-transform:uppercase;letter-spacing:.4px}
.news-card .body-text{margin-top:6px}
.read-more{margin-top:6px;font-size:4.4px;color:var(--gold);text-transform:uppercase;text-decoration:underline}

/* quote */
.quote-eyebrow{position:absolute;left:87px;top:2454px}
.quote-heading{position:absolute;left:87px;top:2465px}
.quote-intro{position:absolute;left:87px;top:2527px;width:190px}
.quote-contacts{position:absolute;left:87px;top:2570px;display:flex;gap:20px}
.quote-contact{display:flex;align-items:center;gap:6px;font-size:4.6px;color:var(--ink)}
.quote-contact .ic{width:24px;height:24px;border-radius:50%;background:var(--light);display:flex;align-items:center;justify-content:center}

.site-footer{position:absolute;left:0;top:2632px;width:654px;height:201px;background:var(--navy);color:#fff}
.quote-form{position:absolute;left:385px;top:2415px;width:182px;height:250px;background:linear-gradient(135deg,#c29d3a 0%,var(--gold) 60%,#a9852a 100%);padding:22px 26px}
.form-title{font-size:10.5px;line-height:13px;color:#fff;font-weight:300}
.form-title strong{display:block;font-weight:700}
.field{margin-top:8px;width:131px;height:22px;background:rgba(255,255,255,.25);border:1px solid rgba(255,255,255,.35);font-size:4.4px;color:#fff;padding:6px 7px}
.field.tall{height:44px}
.form-submit{margin-top:10px;width:131px;height:23px;border-radius:12px;background:#fff;color:var(--gold);font-size:4.6px;font-weight:700;display:flex;align-items:center;justify-content:center;text-transform:uppercase}

.footer-col{position:absolute;top:79px}
.footer-col h4{font-size:7px;font-weight:700;text-transform:uppercase;margin-bottom:8px}
.footer-col p{font-size:4.6px;color:#d6dde8}
.footer-social{display:flex;gap:5px}
.footer-social span{width:5px;height:5px;border-radius:50%;background:var(--gold)}
.footer-line{position:absolute;left:87px;top:132px;width:480px;height:1px;background:rgba(255,255,255,.12)}
.copyright{position:absolute;left:87px;top:146px;font-size:4.4px;color:#c5cedb}
.legal{position:absolute;right:87px;top:146px;font-size:4.4px;color:var(--gold)}
</style>
</head>
<body>

<section class="brand-board">
  <div class="brand-name"><span class="mark"></span>Bluestone Freight</div>
  <div class="board-divider" style="left:492px"></div>
  <div class="board-label" style="left:550px;top:92px">Fonts:</div>
  <div class="font-names">Roboto<br>Sans Serif</div>
  <div class="board-divider" style="left:690px"></div>
  <div class="board-label" style="left:749px;top:88px">Colors:</div>
  <div class="swatch" style="left:750px;background:var(--light)"></div>
  <div class="swatch" style="left:798px;background:var(--navy)"></div>
  <div class="swatch" style="left:845px;background:var(--gold)"></div>
  <div class="swatch" style="left:892px;background:var(--cream)"></div>
  <div class="swatch-code" style="left:744px">#f4f5f7</div>
  <div class="swatch-code" style="left:792px">#14375d</div>
  <div class="swatch-code" style="left:839px">#b7912e</div>
  <div class="swatch-code" style="left:886px">#f9f6ef</div>
</section>

<div class="screen-preview" role="img" aria-label="Desktop view of the homepage hero with a semi truck on a highway at dusk">
  <div class="sp-top"></div>
  <div class="sp-nav"><b>Bluestone Freight</b><div class="sp-links"><span>HOME</span><span>ABOUT US</span><span>SERVICES</span><span>CAREERS</span><span class="sp-cta">CONTACT US</span></div></div>
  <div class="sp-eyebrow">WELCOME TO BLUESTONE FREIGHT</div>
  <div class="sp-h1"><span class="outline">FREIGHT</span><br>BROKERAGE</div>
  <div class="sp-p">We Specialize in: Heavy-Haul, Specialized Loads, Flatbed and Dry Vans.</div>
  <div class="sp-btn"></div>
</div>

<main class="page">
  <div class="hero" role="img" aria-label="Semi truck driving on a highway at dusk"></div>

  <header class="top-bar">
    <div class="social"><span></span><span></span><span></span></div>
    <div class="contact-items">
      <div class="contact-item"><span class="icon-dot"><svg width="5" height="5" viewBox="0 0 10 10"><path d="M2 1l2 2-1 1.5c.8 1.5 1.7 2.4 3 3L7.5 6l2 2-1.5 1.5C4.5 9 1 5.5.5 2.5z" fill="#fff"/></svg></span>+1 555 014 2290</div>
      <div class="contact-item"><span class="icon-dot"><svg width="5" height="4" viewBox="0 0 10 8"><rect x=".5" y=".5" width="9" height="7" fill="none" stroke="#fff"/><path d="M.5.5l4.5 4 4.5-4" fill="none" stroke="#fff"/></svg></span>info@bluestonefreight.com</div>
      <div class="contact-item"><span class="icon-dot"><svg width="4" height="5" viewBox="0 0 8 10"><path d="M4 10S0 5.5 0 3.8a4 4 0 018 0C8 5.5 4 10 4 10z" fill="#fff"/></svg></span>Location goes here</div>
    </div>
  </header>

  <nav class="main-nav">
    <span class="nav-brand">Bluestone Freight</span>
    <div class="nav-links"><span>Home</span><span>About Us</span><span>Services</span><span>Careers</span><span class="nav-cta">Contact Us</span></div>
  </nav>

  <p class="eyebrow hero-eyebrow">Welcome to Bluestone Freight</p>
  <h1 class="hero-title"><span class="outline">FREIGHT</span>BROKERAGE</h1>
  <p class="hero-text">We Specialize in: Heavy-Haul, Specialized Loads, Flatbed and Dry Vans.</p>
  <div class="scroll-btn"><svg width="8" height="10" viewBox="0 0 8 10"><path d="M4 0v9M1 6l3 3 3-3" fill="none" stroke="#fff" stroke-width="1"/></svg></div>

  <!-- about -->
  <p class="eyebrow about-eyebrow">About Bluestone Freight</p>
  <h2 class="heading about-heading">Your Most Reliable<strong>Logistic Solution</strong></h2>
  <p class="body-text about-intro">Lorem ipsum dolor sit amet, consectetur adipiscing elit, sed do eiusmod tempor incididunt ut labore et dolore magna aliqua. Quis ipsum suspendisse ultrices gravida. Risus commodo viverra maecenas accumsan lacus vel facilisis.</p>
  <div class="features">
    <div class="feature" style="left:0"><span class="feature-num">01</span><span class="feature-label">Feature NO1</span></div>
    <div class="feature" style="left:131px"><span class="feature-num">02</span><span class="feature-label">Feature NO2</span></div>
    <div class="feature" style="left:262px"><span class="feature-num">03</span><span class="feature-label">Feature NO3</span></div>
    <div class="feature" style="left:393px"><span class="feature-num">04</span><span class="feature-label">Feature NO4</span></div>
  </div>
  <p class="body-text about-col" style="left:87px">At vero eos et accusamus et iusto odio dignissimos ducimus qui blanditiis praesentium voluptatum deleniti atque corrupti quos dolores et quas molestias excepturi sint occaecati cupiditate non provident, similique sunt in culpa qui.</p>
  <p class="body-text about-col" style="left:372px">Et harum quidem rerum facilis est et expedita distinctio. Nam libero tempore, cum soluta nobis est eligendi optio cumque nihil impedit quo minus id quod maxime placeat facere possimus, omnis voluptas.</p>

  <!-- services -->
  <div class="service-tile tile-navy" style="left:0;top:735px">
    <svg width="34" height="34" viewBox="0 0 34 34" fill="none" stroke="var(--gold)" stroke-width="1.2"><rect x="12" y="4" width="18" height="16"/><path d="M12 20H4v-6l4-4h4M4 24h26M15 4v16M18 4v16M21 4v16M24 4v16M27 4v16"/><circle cx="9" cy="27" r="3"/><circle cx="25" cy="27" r="3"/></svg>
    <span>Heavy Haul</span>
  </div>
  <div class="service-tile tile-gold" style="left:163px;top:735px">
    <svg width="34" height="34" viewBox="0 0 34 34" fill="none" stroke="var(--navy)" stroke-width="1.2"><path d="M6 4l4 0 8 20h10"/><rect x="14" y="8" width="8" height="8" transform="rotate(-20 18 12)"/><rect x="18" y="16" width="9" height="6" transform="rotate(-20 22 19)"/><circle cx="17" cy="27" r="3"/></svg>
    <span>Specialized Loads</span>
  </div>
  <div class="service-tile tile-gold" style="left:0;top:898px">
    <svg width="38" height="34" viewBox="0 0 38 34" fill="none" stroke="var(--navy)" stroke-width="1.2"><path d="M2 20h22v5H2zM24 25V12h6l5 6v7h-11"/><path d="M26 14h4l3 4h-7z"/><rect x="6" y="10" width="10" height="10"/><circle cx="7" cy="27" r="3"/><circle cx="15" cy="27" r="3"/><circle cx="30" cy="27" r="3"/></svg>
    <span>Flatbed</span>
  </div>
  <div class="service-tile tile-navy" style="left:163px;top:898px">
    <svg width="38" height="34" viewBox="0 0 38 34" fill="none" stroke="var(--gold)" stroke-width="1.2"><rect x="2" y="6" width="22" height="18"/><path d="M24 12h6l5 6v6H24z"/><path d="M26 14h4l3 4h-7z"/><circle cx="9" cy="27" r="3"/><circle cx="29" cy="27" r="3"/></svg>
    <span>Dry Vans</span>
  </div>
  <section class="services-panel">
    <p class="eyebrow">Our Services</p>
    <h2 class="heading">What We Offer<strong>To Our Customers</strong></h2>
    <p class="body-text p1">Duis aute irure dolor in reprehenderit in voluptate velit esse cillum dolore eu fugiat nulla pariatur. Excepteur sint occaecat cupidatat non proident, sunt in culpa qui officia deserunt mollit anim id est laborum.</p>
    <p class="body-text p2">Quis autem vel eum iure reprehenderit qui in ea voluptate velit esse quam nihil molestiae consequatur, vel illum qui dolorem.</p>
    <span class="btn btn-gold">Contact Us</span>
  </section>

  <!-- clients -->
  <p class="eyebrow clients-eyebrow">Trusted Customers</p>
  <h2 class="heading clients-heading">Our Clients<strong>&amp; Partners</strong></h2>
  <div class="partner" style="left:291px;top:1146px"><span class="p-circle"></span><span class="p-bar"></span></div>
  <div class="partner" style="left:393px;top:1146px"><span class="p-circle"></span><span class="p-bar"></span></div>
  <div class="partner" style="left:495px;top:1146px"><span class="p-circle"></span><span class="p-bar"></span></div>
  <div class="partner" style="left:291px;top:1184px"><span class="p-circle"></span><span class="p-bar"></span></div>
  <div class="partner" style="left:393px;top:1184px"><span class="p-circle"></span><span class="p-bar"></span></div>
  <div class="partner" style="left:495px;top:1184px"><span class="p-circle"></span><span class="p-bar"></span></div>

  <div class="video-banner" role="img" aria-label="Warehouse worker in a hard hat loading a cardboard box into a truck">
    <svg class="shape" width="480" height="163" viewBox="0 0 480 163"><polygon points="0,0 155,0 315,163 0,163" fill="var(--navy)"/></svg>
    <div class="play-btn"><svg width="10" height="11" viewBox="0 0 10 11"><path d="M1 0l9 5.5L1 11z" fill="#fff"/></svg></div>
    <span class="play-label">See how we do it</span>
  </div>

  <!-- testimonial -->
  <p class="body-text quote-text">"Seque earum rerum hic tenetur a sapiente delectus, ut aut reiciendis voluptatibus maiores alias consequatur aut perferendis doloribus asperiores repellat libero tempore, cum soluta nobis est eligendi."</p>
  <p class="quote-name">Dana Whitfield</p>
  <p class="quote-role">Satisfied Customer</p>
  <p class="eyebrow testi-eyebrow">What our clients say</p>
  <h2 class="heading testi-heading">Clients<strong>Testimonial</strong></h2>
  <div class="quote-mark">&ldquo;</div>

  <!-- why choose -->
  <div class="why-photo" role="img" aria-label="Row of yellow and grey trailers parked at a loading dock"></div>
  <section class="why-panel">
    <p class="eyebrow">Why us</p>
    <h2 class="heading">Why Choosing<strong>Bluestone Freight?</strong></h2>
    <div class="why-item" style="top:135px"><span class="why-icon"><svg width="11" height="12" viewBox="0 0 11 12" fill="none" stroke="var(--gold)"><path d="M5.5 1L1 3v3c0 3 2 5 4.5 5.5C8 11 10 9 10 6V3z"/><path d="M3.5 6l1.5 1.5L8 4.5"/></svg></span><span>Security<br>Guaranteed</span></div>
    <div class="why-item" style="top:173px"><span class="why-icon" style="background:#e3e6ec"><svg width="11" height="11" viewBox="0 0 11 11" fill="none" stroke="var(--navy)"><path d="M1 6l5-5h4v4l-5 5z"/><circle cx="8" cy="3" r="1"/></svg></span><span>Affordable<br>Pricing</span></div>
    <div class="why-item" style="top:211px"><span class="why-icon"><svg width="12" height="10" viewBox="0 0 12 10" fill="none" stroke="var(--gold)"><path d="M1 4l3-3h4l3 3-5 5z"/></svg></span><span>Client<br>Oriented</span></div>
    <span class="btn btn-navy">Contact Us</span>
  </section>
  <div class="years-badge"><b>15</b><span>Years of<br>Experience</span></div>

  <!-- news -->
  <p class="eyebrow news-eyebrow">Blog Posts</p>
  <h2 class="heading news-heading">Company <strong>News</strong></h2>
  <p class="body-text news-intro">Lorem ipsum dolor sit amet, consectetur adipiscing elit, sed do eiusmod tempor incididunt ut labore et dolore.</p>
  <article class="news-card" style="left:87px">
    <div class="news-img" role="img" aria-label="Box truck parked at a warehouse dock" style="background:linear-gradient(120deg,#2c3f55,#5d6b7c 60%,#8794a2)"></div>
    <h3 class="news-title">First Post Title Goes Here</h3>
    <p class="news-meta">June 2022 · By Admin</p>
    <p class="body-text">Lorem ipsum dolor sit amet, consectetur adipiscing elit, sed do eiusmod tempor incididunt ut labore et dolore magna aliqua. Quis ipsum suspendisse ultrices est.</p>
    <p class="read-more">Read more</p>
  </article>
  <article class="news-card" style="left:250px">
    <div class="news-img" role="img" aria-label="Stacked wooden shipping crates in warm light" style="background:linear-gradient(120deg,#5a2a14,#9a5528 55%,#c98a4a)"></div>
    <h3 class="news-title">Second Post Title Goes Here</h3>
    <p class="news-meta">June 2022 · By Admin</p>
    <p class="body-text">Lorem ipsum dolor sit amet, consectetur adipiscing elit, sed do eiusmod tempor incididunt ut labore et dolore magna aliqua. Quis ipsum suspendisse ultrices gravida. Some more text filler for design purpose only sit amet tempor.</p>
    <p class="read-more">Read more</p>
  </article>
  <article class="news-card" style="left:413px">
    <div class="news-img" role="img" aria-label="White delivery van on a road under a blue evening sky" style="background:linear-gradient(180deg,#2a4a80,#5a78ab 55%,#8a8f9a)"></div>
    <h3 class="news-title">Third Post Title Goes Here</h3>
    <p class="news-meta">June 2022 · By Admin</p>
    <p class="body-text">Lorem ipsum dolor sit amet, consectetur adipiscing elit, sed do eiusmod tempor incididunt ut labore et dolore magna aliqua. Quis ipsum suspendisse ultrices est.</p>
    <p class="read-more">Read more</p>
  </article>

  <!-- footer -->
  <footer class="site-footer">
    <div class="footer-col" style="left:87px"><h4>About BSF</h4><p>Specialize in: Heavy-Haul, Specialized Loads, Dry Van, Flatbed</p></div>
    <div class="footer-col" style="left:327px"><h4>Quick Links</h4><p>About &nbsp;|&nbsp; Services &nbsp;|&nbsp; Blog &nbsp;|&nbsp; Contact</p></div>
    <div class="footer-col" style="left:516px"><h4>Follow Us</h4><div class="footer-social"><span></span><span></span><span></span></div></div>
    <div class="footer-line"></div>
    <p class="copyright">© 2022 Bluestone Freight · All rights reserved</p>
    <p class="legal">Privacy Policy &nbsp;|&nbsp; Terms of Use</p>
  </footer>

  <!-- quote -->
  <p class="eyebrow quote-eyebrow">Get in touch</p>
  <h2 class="heading quote-heading">Call or Request<strong>a Free Quote Now</strong></h2>
  <p class="body-text quote-intro">Get in touch with one of Bluestone Freight's representatives through the phone, email or form.</p>
  <div class="quote-contacts">
    <div class="quote-contact"><span class="ic"><svg width="10" height="10" viewBox="0 0 10 10"><path d="M2 1l2 2-1 1.5c.8 1.5 1.7 2.4 3 3L7.5 6l2 2-1.5 1.5C4.5 9 1 5.5.5 2.5z" fill="none" stroke="var(--gold)" stroke-width=".8"/></svg></span>+1 555 014 2290</div>
    <div class="quote-contact"><span class="ic"><svg width="11" height="9" viewBox="0 0 11 9"><rect x=".5" y=".5" width="10" height="8" fill="none" stroke="var(--navy)" stroke-width=".8"/><path d="M.5.5l5 4.5 5-4.5" fill="none" stroke="var(--navy)" stroke-width=".8"/></svg></span>info@bluestonefreight.com</div>
  </div>
  <form class="quote-form">
    <h3 class="form-title">Request Your<strong>Free Quote Now!</strong></h3>
    <div class="field">Name</div>
    <div class="field">Email Address</div>
    <div class="field">Phone Number</div>
    <div class="field tall">Message</div>
    <div class="form-submit">Submit Quote</div>
  </form>
</main>

</body>
</html>
```